We are launching in December, a range of supplements and vitamins.

We have just made an amend to the mission statement and how we are going to give back to society. Please can you add both to the packaging:

Verdant’s purpose is to support health, wellbeing and longevity, so that we can all thrive in the modern world; an environment so alien to that in which we evolved. Embracing technology, research and science, we harness nature’s goodness - enabling us all to love life – naturally.

Twice Kind Promise. For each and every Verdant supplement you take, we provide a supplement to an under nourished child.

For every supplement we sell: £1 goes to the charity ‘Little Lights Fund’ and in addition we provide one healthy meal to an under privileged child in India.

My name is Mark Holloway and I own several companies including www.quartzelle.com (you can check me out on Infopedex – I am not the football referee nor the rocket scientist, but the entrepreneur) . Over the past 2 years I have been writing a book to help people live more healthily and it launches in December. It’s called Verdant Way. While doing my research for the book, I came to realise that most supplements and vitamin products on the market are rubbish! Most are made for profit and not for the benefit of the consumer. I want to change all of that. Howard Pellow is patron of a charity I set up with my brother Paul Holloway and together we have built 11 schools in Asia. I am hoping to get Howards help in getting my supplements to market.

Positioning of our supplements - In a world where so much has changed from the one our bodies were designed to thrive, at Verdant Supplements we are driven by one purpose; to globally provide healthy support to life in the 21st century. While the roots of our wellbeing supplements date back beyond 10,000BC, we embrace modern technology and science, to encapsulate powerful phytonutrients, herbs and other goodness. The essence of which is to promote health, happiness and longevity.

So what are we looking for in the design? Something that stands out. Something that looks professional. A design and concept that can role out across 24 different products. Some products are simple, just one ingredient, such as vitamin D3, Magnesium, Garlic Extracts etc, and others are our own formulas where there are up to 30 different ingredients. You can contact me at any time with questions at Mark@verdantway-example.com

Target Market(s)

Male & Female 20 years plus, mainly UK

Industry/Entity Type

Medical

Logo Text

VERDANT - Sub heading = Thriving Days Gently

Colors

Designer to choose colors to be used in the design.

Requirements
Must have
• see attached powerpoint.
• We have just made an amend to the mission statement and how we are going to give back to society. Please can you add both to the packaging:
• Verdant’s purpose is to support health, wellbeing and longevity, so that we can all thrive in the modern world; an environment so alien to that in which we evolved. Embracing technology, research and science, we harness nature’s goodness - enabling us all to love life – naturally.
• Twice Kind Promise. For each and every Verdant supplement you take, we provide a supplement to an under nourished child.
Nice to have
• see attached powerpoint
Should not have
• see attached powerpoint

```html
<!DOCTYPE html>
<html lang="en">
<head>
<meta charset="UTF-8">
<title>Verdant – Round Magnesium Label</title>
<link rel="stylesheet" href="https://fonts.googleapis.com/css2?family=Jost:wght@300;400;500;600;700&display=swap">
<style>
  :root {
    --page-bg: #efefef;
    --label-bg: #ffffff;
    --ink: #1f1f1f;
    --ink-soft: #555555;
    --ink-light: #6a6a6a;
    --ink-faint: #7a7a7a;
    --rule: #2a2a2a;
  }
  * { margin: 0; padding: 0; box-sizing: border-box; }
  html, body {
    width: 1200px;
    height: 1200px;
    overflow: hidden;
    background: var(--page-bg);
    font-family: "Jost", sans-serif;
    color: var(--ink);
  }
  .canvas {
    position: relative;
    width: 1200px;
    height: 1200px;
  }
  .label {
    position: absolute;
    left: 332px;
    top: 130px;
    width: 536px;
    height: 940px;
    background: var(--label-bg);
    box-shadow: 0 2px 14px rgba(0,0,0,0.06);
  }
  .line {
    position: absolute;
    left: 0;
    width: 100%;
    text-align: center;
    line-height: 1;
    transform: translateY(-50%);
  }
  .brand-name {
    top: 51px;
    font-size: 40px;
    font-weight: 500;
    letter-spacing: 0.42em;
    padding-left: 0.42em;
    color: var(--ink);
  }
  .brand-tagline {
    top: 101px;
    font-size: 22px;
    font-weight: 300;
    letter-spacing: 0.04em;
    color: var(--ink-light);
  }
  .mission {
    position: absolute;
    top: 138px;
    left: 68px;
    width: 400px;
    text-align: center;
    font-size: 12.5px;
    font-weight: 300;
    line-height: 1.45;
    letter-spacing: 0.02em;
    color: var(--ink-faint);
  }
  .product-variant {
    top: 270px;
    font-size: 29px;
    font-weight: 300;
    color: var(--ink-soft);
  }
  .product-name {
    top: 315px;
    font-size: 35px;
    font-weight: 500;
    letter-spacing: 0.3em;
    padding-left: 0.3em;
  }
  .product-description {
    top: 406px;
    font-size: 20px;
    font-weight: 300;
    line-height: 1.42;
    letter-spacing: 0.03em;
    color: var(--ink-soft);
  }
  .element-number {
    top: 490px;
    font-size: 24px;
    font-weight: 300;
    color: var(--ink-soft);
    padding-right: 20px;
  }
  .element-symbol {
    top: 560px;
    font-size: 100px;
    font-weight: 600;
    letter-spacing: -0.02em;
  }
  .benefits {
    position: absolute;
    top: 662px;
    left: 128px;
    width: 280px;
    list-style: none;
  }
  .benefits li {
    height: 40px;
    display: flex;
    align-items: center;
    justify-content: center;
    font-size: 20px;
    font-weight: 300;
    letter-spacing: 0.04em;
    color: var(--ink-soft);
  }
  .benefits li + li { border-top: 2px solid var(--rule); }
  .serving-size {
    top: 814px;
    font-size: 22px;
    font-weight: 600;
    letter-spacing: 0.12em;
    padding-left: 0.12em;
  }
  .net-weight {
    top: 845px;
    font-size: 18px;
    font-weight: 400;
    letter-spacing: 0.04em;
    color: var(--ink-soft);
  }
  .promise {
    position: absolute;
    top: 876px;
    left: 78px;
    width: 380px;
    text-align: center;
    font-size: 12.5px;
    font-weight: 300;
    line-height: 1.45;
    letter-spacing: 0.02em;
    color: var(--ink-faint);
  }
  .promise strong { font-weight: 500; color: var(--ink-soft); }
</style>
</head>
<body>
<main class="canvas">
  <section class="label">
    <div class="line brand-name">VERDANT</div>
    <div class="line brand-tagline">thriving days gently</div>

    <p class="mission">Verdant’s purpose is to support health, wellbeing and longevity, so that we can all thrive in the modern world; an environment so alien to that in which we evolved. Embracing technology, research and science, we harness nature’s goodness – enabling us all to love life – naturally.</p>

    <div class="line product-variant">round</div>
    <h1 class="line product-name">MAGNESIUM</h1>
    <p class="line product-description">tailored supplement for<br>exercise and improve<br>bone and teeth health</p>

    <div class="line element-number">12</div>
    <div class="line element-symbol">Mg</div>

    <ul class="benefits">
      <li>reduce tiredness</li>
      <li>electrolyte balance</li>
      <li>improves heart health</li>
    </ul>

    <div class="line serving-size">SERVING SIZE 60</div>
    <div class="line net-weight">Weight 275 mg</div>

    <p class="promise"><strong>Twice Kind Promise.</strong> For each and every Verdant supplement you take, we provide a supplement to an under nourished child.</p>
  </section>
</main>
</body>
</html>
```